Poster for Ballet Recital Tomasito y el Espejo Encantado

We need a poster for a ballet performance, we will be presenting "Tomasito y el Espejo Encantado".
We need something that looks magical, the word Tomasito as the main title in 3D gold texture and the text y el Espejo Encantado way smaller. We have included a reference of the Brelvo movie, just because we like the starry night background and the glowing moon. We don't want the two characters nor the flying carpet, because we will be adding a photo later.
The idea is for the poster to look magical, mysterious but fun. We want people to get the idea that the show will be very entertaining and worth their money.

Font styles to use
Decorative
Script

Colors

Designer to choose colors to be used in the design.

Requirements
Must have
• The title: Tomasito y el Espejo Encantado
• It must also include space for adding the ballet company logo, the dates, times and prices.
Nice to have
• Magical feel
Should not have
• Any photo or character illustration

```html
<!DOCTYPE html>
<html lang="es">
<head>
<meta charset="utf-8">
<title>Tomasito y el Espejo Encantado — Poster</title>
<link href="https://fonts.googleapis.com/css2?family=Kaushan+Script&family=Marcellus&family=Jost:wght@300;400&display=swap" rel="stylesheet">
<style>
  :root {
    --page-bg: #e6e6ea;
    --sky-top: #5b5f9e;
    --sky-glow: #8a86bd;
    --sky-low: #4b5193;
    --night-ground: #1d2340;
    --moon: rgba(200, 200, 235, 0.28);
    --gold: #e9ad3c;
    --gold-light: #f7d477;
    --gold-deep: #b47a16;
    --ink-light: #ffffff;
  }
  * { box-sizing: border-box; margin: 0; padding: 0; }
  html, body { width: 1200px; height: 1200px; overflow: hidden; }
  body { background: var(--page-bg); position: relative; }

  .poster {
    position: absolute;
    left: 258px; top: 60px;
    width: 687px; height: 1047px;
    overflow: hidden;
    background:
      radial-gradient(ellipse 70% 45% at 35% 18%, var(--sky-glow) 0%, transparent 70%),
      linear-gradient(180deg, var(--sky-top) 0%, var(--sky-low) 70%, #3e4483 100%);
  }
  .poster__sky { position: absolute; inset: 0; }
  .poster__moon {
    position: absolute;
    left: 105px; top: 273px;
    width: 504px; height: 504px;
    border-radius: 50%;
    background: var(--moon);
  }
  .poster__horizon { position: absolute; left: 0; top: 700px; width: 687px; height: 130px; }
  .poster__ground {
    position: absolute; left: 0; top: 826px; width: 687px; height: 221px;
    background: var(--night-ground);
  }

  .presenter {
    position: absolute; left: 0; right: 0; top: 64px;
    text-align: center;
    font-family: "Marcellus", serif;
    color: var(--ink-light);
    font-size: 34px; line-height: 46px;
  }

  .title {
    position: absolute; left: 0; right: 0; top: 240px;
    text-align: center;
    font-family: "Kaushan Script", cursive;
    font-size: 136px; line-height: 1;
    white-space: nowrap;
    background: linear-gradient(180deg, var(--gold-light) 0%, var(--gold) 45%, var(--gold-deep) 100%);
    -webkit-background-clip: text; background-clip: text;
    color: transparent;
    filter: drop-shadow(3px 4px 0 #8d5c10) drop-shadow(0 2px 4px rgba(0,0,0,0.35));
  }
  .subtitle {
    position: absolute; left: 214px; top: 428px;
    font-family: "Marcellus", serif;
    color: var(--gold);
    font-size: 35px; line-height: 48px;
    letter-spacing: 4px;
  }

  .event-date {
    position: absolute; left: 0; right: 0; top: 588px;
    text-align: center;
    font-family: "Marcellus", serif;
    color: var(--ink-light);
    font-size: 35px; letter-spacing: 6px;
  }
  .event-place {
    position: absolute; left: 0; right: 0; top: 650px;
    text-align: center;
    font-family: "Marcellus", serif;
    color: var(--ink-light);
    font-size: 26px;
  }

  .tickets {
    position: absolute; left: 124px; top: 796px; width: 440px;
    font-family: "Jost", sans-serif; font-weight: 300;
    color: var(--gold);
  }
  .tickets__heading {
    text-align: center; font-size: 31px; letter-spacing: 1px; margin-bottom: 14px;
  }
  .price-row {
    display: flex; align-items: flex-end;
    font-size: 30px; line-height: 36px; height: 50px;
  }
  .price-row__line {
    flex: 1; border-bottom: 2px solid var(--gold); margin-bottom: 6px; margin-left: 2px;
  }
</style>
</head>
<body>
  <main class="poster">
    <svg class="poster__sky" role="img" aria-label="Starry night sky" viewBox="0 0 687 1047"></svg>
    <div class="poster__moon"></div>
    <svg class="poster__horizon" role="img" aria-label="Dark mountain silhouette on the horizon" viewBox="0 0 687 130" preserveAspectRatio="none">
      <defs>
        <linearGradient id="horizon-fade" x1="0" y1="0" x2="0" y2="1">
          <stop offset="0" stop-color="#1d2340" stop-opacity="0"/>
          <stop offset="0.55" stop-color="#1d2340" stop-opacity="0.75"/>
          <stop offset="1" stop-color="#1d2340"/>
        </linearGradient>
      </defs>
      <rect width="687" height="130" fill="url(#horizon-fade)"/>
    </svg>
    <div class="poster__ground"></div>

    <header class="presenter">
      <p class="presenter__company">COMPANY LOGO</p>
      <p class="presenter__line">PRESENTS</p>
    </header>

    <h1 class="title">Tomasito</h1>
    <p class="subtitle">y el Espejo<br>Encantado</p>

    <p class="event-date">FEBRUARY 25, 2019</p>
    <p class="event-place">TIME AND PLACE</p>

    <section class="tickets">
      <h2 class="tickets__heading">TICKET PRICES:</h2>
      <div class="price-row"><span>VIP A</span><span class="price-row__line"></span></div>
      <div class="price-row"><span>VIP B</span><span class="price-row__line"></span></div>
      <div class="price-row"><span>BALCONY</span><span class="price-row__line"></span></div>
    </section>
  </main>
</body>
</html>
```